Redesign two existing website pages and one new landing page for dental office

I need to redesign two webpages on my dental website, the Home page (http://brelvoortdental.com) and the Dental Implant Services page (http://www.brelvoortdental.com/dental-implant-services) and also create a landing page for the Dental Implant Services page.

Please use the same color scheme, slogans and subtitles for the redesign pages and create a reserved video spot on each page. The video spots should not be too big but not too small either and positioned in a central key location on each of the pages. The final redesigned pages should communicate leadership, confidence and trust.

The new landing page for the Dental implant Services page must not have any hyperlinks on the page and must entice the viewer to give name and email before downloading a "Free" eBook called "Is a Fresh Smile Worth Waiting For?" Any added photo images to this new page must be smiling.
Updates

Project Deadline Extended Reason: I got feedback that my project was not long enough so I'm extending it by 5 days. Added Thursday, April 16, 2015

Target Market(s)

People who are middle-age to seniors.

Industry/Entity Type

Dental

Coding

Coded - Design and coding required

Number of Pages Required

3 page

Requirements
Must have
• Compatible with existing website colors and theme.

```html
<!DOCTYPE html>
<html lang="en">
<head>
<meta charset="utf-8">
<title>Brelvoort Dental Care</title>
<link href="https://fonts.googleapis.com/css2?family=Lato:wght@400;700&display=swap" rel="stylesheet">
<style>
:root{
  --ink:#333;
  --muted:#777;
  --topbar:#333;
  --green-dark:#2d4c42;
  --green:#3a6a5c;
  --green-soft:#7fa395;
  --card:#eef4f2;
  --white:#fff;
  --footer-text:#b9c9c3;
}
*{margin:0;padding:0;box-sizing:border-box}
html,body{width:667px;height:1200px;overflow:hidden}
body{font-family:'Lato',Arial,sans-serif;color:var(--ink);background:var(--white);position:relative}
.abs{position:absolute}
.topbar{left:0;top:0;width:667px;height:21px;background:var(--topbar);color:#aaa;font-size:7.5px;line-height:21px}
.topbar .links{left:61px;top:0;display:flex;align-items:center;height:21px}
.topbar .links span{margin-right:14px;display:flex;align-items:center;gap:5px}
.ico-phone{width:5px;height:9px;border:1px solid #999;border-radius:1px;display:block}
.ico-form{width:7px;height:9px;border:1px solid #999;display:block}
.topbar .call{right:131px;top:0;white-space:nowrap}
.topbar .call b{color:#fff;font-weight:400}
.social{left:544px;top:5px;display:flex;gap:5px}
.social i{width:11px;height:11px;border-radius:50%;background:#fff;opacity:.85;display:block}
.header{left:0;top:21px;width:667px;height:71px;border-bottom:1px solid #ddd}
.brand{left:62px;top:30px;font-size:16px;color:var(--green);display:flex;align-items:center;gap:6px;white-space:nowrap}
.brand .dot{width:8px;height:8px;border-radius:50%;background:var(--green-soft)}
.nav{left:264px;top:0;display:flex;height:57px;font-size:7.5px;text-transform:uppercase}
.nav a{color:#555;text-decoration:none;padding:0 8px;line-height:52px}
.nav a.active{background:#e1efeb;color:var(--green-dark);font-weight:700;border-bottom:3px solid var(--green-dark)}
.hero{left:0;top:92px;width:667px;height:291px;background:linear-gradient(90deg,#8fb66e 0%,#c9dfa4 40%,#e9eee4 70%,#cdd8c8 100%);border-bottom:2px solid var(--green-dark)}
.hero-photo{left:305px;top:20px;width:345px;height:271px;background:linear-gradient(180deg,#d9cfc4,#b9a99a);border-radius:4px;opacity:.75}
.hero h1{left:61px;top:107px;font-weight:400;font-size:21px;line-height:26px;color:#333}
.hero h1 strong{color:var(--green-dark);font-weight:700;display:block}
.btn-dark{left:61px;top:171px;background:#222;color:#fff;font-size:9px;font-weight:700;padding:8px 10px;text-transform:uppercase;border-radius:2px}
.dots{left:66px;top:262px;display:flex;gap:2px}
.dots i{width:5px;height:5px;border-radius:50%;background:#7a8a70;display:block}
.dots i:first-child{background:#222}
.col{top:418px;width:170px}
.col h2{font-size:11px;font-weight:400;text-transform:uppercase;color:#333}
.thumb{margin-top:10px;width:165px;height:78px;border:3px solid #fff;box-shadow:0 0 2px #bbb}
.col h3{font-size:8.8px;font-weight:400;margin-top:12px}
.col p{font-size:6.6px;color:var(--muted);line-height:11px;margin-top:3px}
.col .more{font-size:6.6px;font-weight:700;margin-top:3px;color:#222}
.video{width:165px;height:132px;margin-top:10px;border:3px solid #fff;box-shadow:0 0 2px #bbb;background:linear-gradient(135deg,#c8cdd2,#e7d8c8);position:relative}
.video svg{position:absolute;left:66px;top:48px}
.band{left:0;top:630px;width:667px;height:53px;background:var(--green-dark);color:#fff}
.band p{left:72px;top:17px;font-size:12px;white-space:nowrap}
.band .btn{left:464px;top:13px;background:#fff;color:#222;font-size:9.5px;padding:6px 9px}
.services-title{left:0;top:705px;width:667px;text-align:center;font-size:21px;color:var(--green)}
.services-title b{color:var(--green-dark)}
.services-intro{left:60px;top:738px;width:547px;text-align:center;font-size:7.5px;color:var(--muted);line-height:12px}
.card{top:782px;width:132px;height:161px;background:var(--card);padding:0 8px}
.card .avatar{width:54px;height:54px;border-radius:50%;margin:13px auto 0;border:2px solid #ccc;background:linear-gradient(180deg,#e7cdb8,#c59a80)}
.card h3{font-size:10.5px;font-weight:400;margin-top:12px;color:#333;white-space:nowrap}
.card ul{list-style:none;font-size:7.2px;line-height:12.3px;margin-top:6px;color:#444}
.card li{white-space:nowrap}
.footer{left:0;top:970px;width:667px;height:207px;background:var(--green-dark);color:var(--footer-text)}
.footer h4{font-size:10.5px;font-weight:400;color:#fff;text-transform:uppercase;position:absolute;top:27px}
.f-photo{left:61px;top:50px;width:56px;height:50px;background:linear-gradient(180deg,#e4d6ca,#b8a394)}
.f-text{font-size:6.8px;line-height:11px}
.post{left:253px;display:flex;gap:7px;width:160px}
.date{flex:none;width:34px;height:34px;background:#223a33;color:#fff;text-align:center;font-size:12px;padding-top:4px;line-height:12px}
.date small{display:block;font-size:7px;color:#ccc}
.post p{font-size:6.8px;line-height:11px;padding-top:5px;width:118px}
.map{left:445px;top:50px;width:162px;height:67px;background:linear-gradient(135deg,#e9ecd9,#d7e0e6)}
.contact{left:445px;top:126px;font-size:6.8px;line-height:11px;border-collapse:collapse}
.contact td{vertical-align:top;padding-right:6px}
.copy{left:0;top:1177px;width:667px;height:23px;line-height:23px;text-align:center;font-size:6.8px;color:#666;background:#fff}
</style>
</head>
<body>

<div class="abs topbar">
  <div class="abs links"><span><i class="ico-phone"></i>Get Dr.Brelvoort Mobile App</span><span><i class="ico-form"></i>Patient online Forms</span></div>
  <div class="abs call">Call Us Today..! <b>(281) 555 0142</b></div>
  <div class="abs social" aria-hidden="true"><i></i><i></i><i></i><i></i></div>
</div>

<div class="abs header">
  <div class="abs brand"><span class="dot"></span>Brelvoort Dental Care</div>
  <nav class="abs nav">
    <a class="active">Home</a><a>About Us</a><a>Dental Services</a><a>Blog</a><a>Contact Us</a><a>Testimonials</a>
  </nav>
</div>

<section class="abs hero">
  <div class="abs hero-photo" role="img" aria-label="Smiling family of four posing together"></div>
  <h1 class="abs">Life-Changing Family <strong>Dental Care In Sugar Land</strong></h1>
  <div class="abs btn-dark">Request An Appointment</div>
  <div class="abs dots"><i></i><i></i><i></i><i></i></div>
</section>

<div class="abs col" style="left:61px">
  <h2>Dental Hygiene Services</h2>
  <div class="thumb" role="img" aria-label="Children brushing their teeth" style="background:linear-gradient(135deg,#e8e3dd,#c9d7e3)"></div>
  <h3>Achieve Better Health With Prevention</h3>
  <p>Lorem ipsum dolor sit amet, consectetur adipiscing elit, sed do eiusmod tempor incididunt ut labore et dolore magna aliqua...</p>
  <div class="more">Read More »</div>
</div>
<div class="abs col" style="left:250px">
  <h2>Dental Emergency Services</h2>
  <div class="thumb" role="img" aria-label="Woman holding her cheek in tooth pain" style="background:linear-gradient(135deg,#efe9e3,#d89a6c)"></div>
  <h3>Stop Pain From Tooth Trauma &amp; Infection</h3>
  <p>Lorem ipsum dolor sit amet, consectetur adipiscing elit, sed do eiusmod tempor incididunt ut labore et dolore magna aliqua...</p>
  <div class="more">Read More »</div>
</div>
<div class="abs col" style="left:440px">
  <h2>Welcome To Our Practice</h2>
  <div class="video" role="img" aria-label="Video of a dentist examining a patient">
    <svg width="30" height="30" viewBox="0 0 30 30" aria-hidden="true"><circle cx="15" cy="15" r="15" fill="#555" opacity=".7"/><path d="M11 8 L22 15 L11 22 Z" fill="#fff"/></svg>
  </div>
</div>

<div class="abs band">
  <p class="abs">Comprehensive Family Dentistry in One Sugar Land Dental Office!</p>
  <div class="abs btn">Schedule An Appointment</div>
</div>

<h2 class="abs services-title" style="font-weight:400">OUR <b>SERVICES</b></h2>
<p class="abs services-intro">Lorem ipsum dolor sit amet, consectetur adipiscing elit, sed do eiusmod tempor incididunt ut labore et dolore magna aliqua.<br>Ut enim ad minim veniam, quis nostrud exercitation ullamco laboris nisi consequat.</p>

<div class="abs card" style="left:65px">
  <div class="avatar" role="img" aria-label="Smiling senior woman"></div>
  <h3>Beautiful Dentures</h3>
  <ul><li>What is a Denture?</li><li>Who Needs a Denture?</li><li>Just How Are Dentures Made?</li></ul>
</div>
<div class="abs card" style="left:203px">
  <div class="avatar" role="img" aria-label="Smiling woman"></div>
  <h3>Cosmetic Dentistry</h3>
  <ul><li>Whiten Your Teeth</li><li>Porcelain Veneers</li><li>Clear Aligner Therapy Orthodontics</li></ul>
</div>
<div class="abs card" style="left:341px">
  <div class="avatar" role="img" aria-label="Smiling woman with dark hair"></div>
  <h3>Dental Implant Services</h3>
  <ul><li>Anchorage to the jaw bone</li><li>Replaces 1 or more missing teeth</li><li>Stabilizes loose, floppy dentures</li></ul>
</div>
<div class="abs card" style="left:479px">
  <div class="avatar" role="img" aria-label="Smiling relaxed woman"></div>
  <h3>Sedation Dentistry</h3>
  <ul><li>Control Dental Fear with</li><li>Sedation Dentistry</li><li>Dental Pain Management</li><li>Relaxed and Tranquil Treatment</li></ul>
</div>

<footer class="abs footer">
  <h4 style="left:61px">Don't Wait 'Til It Hurts!</h4>
  <div class="abs f-photo" role="img" aria-label="Woman with toothache"></div>
  <p class="abs f-text" style="left:124px;top:50px;width:98px">Lorem ipsum dolor sit amet, consectetur adipiscing elit, sed do eiusmod tempor incididunt ut labore et dolore magna aliqua...</p>
  <p class="abs f-text" style="left:61px;top:105px;width:165px">Lorem ipsum dolor sit amet, consectetur adipiscing elit, sed do eiusmod tempor incididunt ut labore et dolore magna aliqua...</p>

  <h4 style="left:253px">Recent Blog Posts</h4>
  <div class="abs post" style="top:50px"><div class="date">15<small>April</small></div><p>Conscious Sedation: A Way to Deal with Anxiety at the Dentist's Office</p></div>
  <div class="abs post" style="top:89px"><div class="date">15<small>April</small></div><p>Pediatric Dentists and Their Importance in Today's World</p></div>
  <div class="abs post" style="top:128px"><div class="date">15<small>April</small></div><p>Conscious Sedation: A Way to Deal with Anxiety at the Dentist's Office</p></div>

  <h4 style="left:445px">Contact Us</h4>
  <div class="abs map" role="img" aria-label="Map showing the office location"></div>
  <table class="abs contact">
    <tr><td>Address:</td><td>2480 Orchard Bend Rd, Ste. #120, Sugar<br>Land, TX 77478</td></tr>
    <tr><td>Email:</td><td>info@brelvoortdental.com</td></tr>
    <tr><td>Phone:</td><td>(281) 555 0142</td></tr>
    <tr><td>Fax:</td><td>(281) 555 0142</td></tr>
  </table>
</footer>

<div class="abs copy">Copyrights © 2015 Brelvoort Dental Care, Harborline Medical Center.com - All Rights reserved</div>

</body>
</html>
```